One of Australia's fastest growing energy maintenance contractors needs a new website

www.panelbrite.com.au
Our business has evolved over the past years and now our website is no longer relevant.
We clean solar panels and we vacuum roof gutters.
We clean solar panels on the roofs of residential houses right up to billion dollar solar farms with in excess of 1 million panels. We offer thermal image testing and bird proofing for our residential and commercial clients and thermal drone imaging services for our solar farm clients.
We vacuum clean roof gutters (using a LoftSuk) on the residential house next door right up to enormous private and public schools, colleges, shopping centres, strat complexes and commercial buildings.
When first built our business had more of a domestic residential skew and the website reflected that. While that is still part of our core business we are now bidding on and have secured large government, commercial and infrastructure contracts and our new website needs to reflect our growth and our new business. We need a new site that it optimised for both desktop ad phone viewing as our latest figures showed that 73% of people visiting our site are on mobile phones. We have an extensive amount of data on Trekmetrics available as well as Bidlinks. Both that would also need integrating with the site along with a few other plugins such as Kembo Chat IQ, Friendwall etc along with SEO key words etc. We are also the winner and finalists over multiple years of the small business of the year awards and we like to proudly and prominently display those on our site.
We are looking for a new site with a modern professional feel / theme
There is a definitive break in our business between the solar Panel cleaning clients and the gutter cleaning clients so we would like a home page that begins with a simple choice:
Solar Panel Cleaning – Gutter Cleaning
With a professional full screen background image (we have hundreds to choose from) and along the bottom a small area with rights reserved etc, phone number etc (at some point in the future we will split these into two businesses but for now it’s what we have).
After that selection is made we would like a repeat of that same scenario but the selection is:
If it’s Solar Panel Cleaning
(new background image)
Government – Infrastructure – Commercial – Residential
If it’s Gutter Cleaning
(new background image)
Government – Strata – Commercial – Residential
After making those choices then onto the relevant pages with background images relevant to each sector and a them that suits (on the residential we would like to keep the link to our trekmetrics reviews) - We will provide copy / text for each relevant page.
Other than that, a menu inclusive of the above and:
Resellers Portal – we will provide a link to this from Kembo CRM)
Customer portal (we will supply a link to this from our booking system)
We also need a page for our Solar Resellers / Partners page but we will give them a link to this, it won’t be listed on the site.
Request a quote page (Again we will provide information from Kembo as this will be linked to the CRM)
Standard contact us page inclusive of phone numbers, address and fields supplied from CRM
Sydney – 02 7391 5084
Southern Highlands – 02 4863 1507
Goulburn – 02 4863 1507
Canberra – 02 6178 3045
Wollongong – 02 4239 7615
sales@panelbrite.com.au
Head Office - Ferndell NSW 2583
ABN: 48762093115
Responsive Design: Optimized for desktop and mobile (73% mobile visitors).
Fast Loading Speed: Optimized for performance.
Smooth Transition Animations: For service and category selection.
Sticky Contact Bar: Always accessible at the bottom of mobile screens for quick calls.
SEO Optimization: Focused on government tenders, large-scale commercial contracts, and infrastructure projects.
Integrations
Trekmetrics & Trekmetrics Bidlinks.
Kembo Chat IQ.
Friendwall Beacon.
SEO tools and keyword optimization.
Many many more images available if needed

```html
<!DOCTYPE html>
<html lang="en">
<head>
<meta charset="utf-8">
<title>PanelBrite – Solar Cleaning &amp; Vacuum Roof Gutters Cleaning</title>
<link href="https://fonts.googleapis.com/css2?family=Outfit:wght@300;400;500;600;700&display=swap" rel="stylesheet">
<style>
:root{
  --navy:#0b4f8a;
  --blue:#1b8fd6;
  --blue-deep:#0a5aa3;
  --sky:#dceaf5;
  --ink:#1d3557;
  --text:#2b2f36;
  --muted:#5b6673;
  --grey:#eef1f4;
  --white:#ffffff;
  --star:#f4b400;
}
*{box-sizing:border-box;margin:0;padding:0}
html,body{width:1200px;height:4190px;overflow:hidden}
body{font-family:'Outfit',sans-serif;color:var(--text);background:var(--white);position:relative}
.abs{position:absolute}
.photo{position:absolute}

/* header */
.site-header{position:absolute;left:0;top:0;width:1200px;height:75px;background:var(--white);z-index:5}
.brand{position:absolute;display:flex;align-items:center;gap:10px;color:var(--navy);font-weight:600}
.brand .mark{background:var(--blue);display:block}
.site-header .brand{left:106px;top:18px;font-size:27px}
.site-header .brand .mark{width:36px;height:36px}
.main-nav a{position:absolute;top:30px;font-size:14px;color:var(--ink);text-decoration:none}
.quote-btn{position:absolute;right:0;top:0;width:208px;height:75px;background:linear-gradient(90deg,var(--blue-deep),var(--blue));clip-path:polygon(18px 0,100% 0,100% 100%,0 100%);color:#fff;font-size:15px;display:flex;align-items:center;justify-content:center;padding-left:10px}

/* hero */
.hero-photo{left:0;top:75px;width:1200px;height:675px;background:linear-gradient(180deg,#cfe2f1 0%,#a9c6dd 45%,#6d8aa6 100%)}
.hero-tag{position:absolute;left:470px;top:139px;width:280px;height:26px;background:var(--navy);clip-path:polygon(8px 0,100% 0,calc(100% - 8px) 100%,0 100%);color:#fff;font-size:15px;font-weight:600;letter-spacing:2px;display:flex;align-items:center;justify-content:center}
.hero-title{position:absolute;left:0;width:1200px;top:165px;text-align:center;font-size:47px;font-weight:600;line-height:51px;color:var(--blue-deep)}
.hero-sub{position:absolute;left:0;width:1200px;top:283px;text-align:center;font-size:15px;color:var(--ink)}
.btn{position:absolute;height:49px;background:var(--blue-deep);color:#fff;font-weight:600;font-size:15px;display:flex;align-items:center;justify-content:center;gap:8px;letter-spacing:.3px}
.btn .notch{position:absolute;left:0;top:0;width:26px;height:49px;background:var(--blue)}
.btn span{padding-left:22px}

/* welcome */
.welcome-mark{left:580px;top:692px;width:40px;height:40px;background:var(--blue)}
.section-title{position:absolute;left:0;width:1200px;text-align:center;font-weight:600;color:var(--ink)}
.welcome-title{top:750px;font-size:42px;letter-spacing:2px;color:var(--blue)}
.welcome-title b{color:var(--navy);font-weight:600}
.lead{position:absolute;left:0;width:1200px;text-align:center;font-size:16px;line-height:27px;color:var(--text)}
.service-card{position:absolute;top:907px;width:490px;height:342px;overflow:visible}
.service-card .img{position:absolute;inset:0}
.service-card .label{position:absolute;left:0;width:100%;top:250px;text-align:center;color:#fff;font-size:27px;font-weight:600}
.service-card .icon{position:absolute;left:204px;top:310px;width:82px;height:82px;border-radius:50%;background:var(--blue);border:5px solid #fff;box-shadow:0 0 0 2px var(--blue)}
.corner{position:absolute;border-color:var(--blue);border-style:solid}

/* solar section */
.solar-band{left:0;top:1353px;width:1200px;height:655px;background:linear-gradient(180deg,#1f9be0 0%,#1586cf 60%,#0f72b8 100%)}
.solar-title{top:1410px;font-size:42px;color:#fff}
.solar-sub{top:1476px;color:#fff;font-size:16px}
.hex{position:absolute;top:1537px;width:239px;height:268px;clip-path:polygon(50% 0,100% 25%,100% 75%,50% 100%,0 75%,0 25%)}
.hex .label{position:absolute;left:0;width:100%;top:182px;text-align:center;color:#fff;font-size:23px;font-weight:600}

/* gutter section */
.gutter-bg{left:0;top:2008px;width:1200px;height:623px;background:var(--grey)}
.gutter-title{position:absolute;left:117px;top:2080px;font-size:40px;font-weight:600;color:var(--ink)}
.gutter-text{position:absolute;left:117px;top:2142px;width:330px;font-size:16px;line-height:27px}
.gutter-photo{left:0;top:2200px;width:610px;height:431px;background:linear-gradient(180deg,rgba(238,241,244,0) 0%,#9fb3c8 35%,#c3643d 78%,#b0532f 100%)}
.tile{position:absolute;width:304px;height:200px}
.tile .label{position:absolute;left:26px;bottom:22px;color:#fff;font-size:22px;font-weight:600}

/* testimonials */
.testi-title{top:2690px;font-size:40px}
.side-card{position:absolute;top:2818px;width:912px;left:161px;height:245px;background:#fff;border:1px solid #e1e6ec}
.side-card p{position:absolute;top:62px;width:110px;font-size:11px;line-height:19px;color:var(--muted)}
.side-card .g{position:absolute;right:22px;bottom:22px;width:16px;height:16px;border-radius:50%;border:3px solid var(--blue)}
.main-quote{position:absolute;left:314px;top:2781px;width:585px;height:317px;background:var(--navy);color:#fff;text-align:center}
.main-quote .qm{font-size:90px;line-height:90px;font-weight:700;margin-top:18px;height:64px}
.main-quote p{width:510px;margin:20px auto 0;font-size:16px;line-height:26px}
.stars{margin-top:14px;color:var(--star);font-size:22px;letter-spacing:2px}
.main-quote .name{font-size:19px;margin-top:2px}
.main-quote .g{position:absolute;right:28px;bottom:22px;width:36px;height:36px;border-radius:50%;background:#fff;border:6px solid #fff;box-shadow:inset 0 0 0 4px var(--blue)}
.arrow{position:absolute;top:2912px;width:50px;height:50px;border-radius:50%;background:#fff;box-shadow:0 2px 10px rgba(0,0,0,.12);display:flex;align-items:center;justify-content:center}

/* quote form */
.houses-photo{left:0;top:3114px;width:1200px;height:406px;background:linear-gradient(180deg,#f2f5f8 0%,#b7c8d8 40%,#6b86a3 100%)}
.quote-box{position:absolute;left:177px;top:3320px;width:862px;height:493px;background:linear-gradient(90deg,var(--blue-deep),#1b95d8);border-radius:80px 0 80px 0}
.quote-title{position:absolute;left:0;width:100%;top:50px;text-align:center;font-size:36px;font-weight:600;color:#fff}
.field{position:absolute;height:50px;background:#fff;display:flex;align-items:center;gap:12px;padding-left:20px;font-size:14px;color:var(--text)}
.field svg{flex:none}
.field.msg{align-items:flex-start;padding-top:16px}

/* footer */
.footer-brand{left:120px;top:3925px;width:190px;text-align:center;color:var(--blue-deep);font-size:32px;font-weight:600}
.footer-mark{left:190px;top:3872px;width:50px;height:50px;background:var(--blue)}
.socials{position:absolute;left:130px;top:3992px;display:flex;gap:8px}
.socials span{width:28px;height:28px;border-radius:50%;background:var(--navy);display:block}
.fcol{position:absolute;top:3896px}
.fcol h4{font-size:18px;letter-spacing:2px;font-weight:600;color:var(--ink);padding-bottom:10px;border-bottom:2px solid #bcd6ea;display:inline-block;min-width:130px}
.fcol ul{list-style:none;margin-top:16px}
.fcol li{font-size:14px;line-height:23px;color:var(--muted);display:flex;align-items:center;gap:8px}
.copyright{position:absolute;left:0;top:4138px;width:1200px;height:52px;background:var(--grey);text-align:center;line-height:52px;font-size:13px;color:var(--text)}
</style>
</head>
<body>

<header class="site-header">
  <div class="brand"><span class="mark"></span>PanelBrite</div>
  <nav class="main-nav">
    <a style="left:374px">Solar Cleaning</a>
    <a style="left:493px">Gutter Cleaning</a>
    <a style="left:623px">Resellers Portal</a>
    <a style="left:753px">Customer portal</a>
    <a style="left:889px">Contact Us</a>
  </nav>
  <div class="quote-btn">Request a Quote &nbsp;›</div>
</header>

<section class="hero">
  <div class="photo hero-photo" role="img" aria-label="Two workers on rooftops: one scrubbing solar panels, one pressure washing a tiled roof, under a pale blue sky"></div>
  <div class="hero-tag">WELCOME TO PANELBRITE</div>
  <h1 class="hero-title">Solar Cleaning &amp; Vacuum<br>Roof Gutters Cleaning</h1>
  <p class="hero-sub">We have a detailed knowledge of the cleaning &amp; testing of Solar Panels</p>
  <div class="btn" style="left:517px;top:320px;width:192px"><i class="notch"></i><span>GET A QUOTE ›</span></div>
  <svg class="abs" style="left:0;top:595px" width="1200" height="160" viewBox="0 0 1200 160">
    <polygon points="0,155 600,10 1200,155 1200,160 0,160" fill="#fff"/>
    <polyline points="0,155 600,10 1200,155" fill="none" stroke="#0b5fa8" stroke-width="9"/>
  </svg>
</section>

<section class="welcome">
  <div class="abs welcome-mark"></div>
  <h2 class="section-title welcome-title">Welcome to <b>PanelBrite</b></h2>
  <p class="lead" style="top:808px">Lorem ipsum dolor sit amet, consectetur adipiscing elit, sed do eiusmod tempor incidi-<br>dunt ut labore et dolore magna aliqua Quis ipsum suspendisse</p>

  <div class="corner" style="left:94px;top:893px;width:86px;height:90px;border-width:8px 0 0 8px"></div>
  <div class="corner" style="left:1020px;top:1175px;width:86px;height:90px;border-width:0 8px 8px 0"></div>

  <div class="service-card" style="left:107px">
    <div class="img" role="img" aria-label="Worker cleaning rows of solar panels on a rooftop against a blue sky" style="background:linear-gradient(180deg,#5aa6e0 0%,#3d7fbf 55%,#1f4f86 100%)"></div>
    <div class="label">Solar Panel Cleaning</div>
    <div class="icon"></div>
  </div>
  <div class="service-card" style="left:603px">
    <div class="img" role="img" aria-label="Worker pressure washing a terracotta tiled roof beside a satellite dish" style="background:linear-gradient(180deg,#6ab0e6 0%,#8fa0ad 50%,#6e5a52 100%)"></div>
    <div class="label">Roof Gutter Cleaning</div>
    <div class="icon"></div>
  </div>
  <div class="abs" style="left:580px;top:1078px;width:40px;height:40px;background:#fff;clip-path:polygon(50% 0,100% 25%,100% 75%,50% 100%,0 75%,0 25%)"></div>
  <div class="abs" style="left:599px;top:1280px;width:1px;height:73px;background:#c9d3dd"></div>
</section>

<section class="solar">
  <div class="photo solar-band" role="img" aria-label="Blue tinted solar panel grid with a technician in the background"></div>
  <h2 class="section-title solar-title">Solar Panel Cleaning</h2>
  <p class="lead solar-sub">Lorem ipsum dolor sit amet, consectetur adipiscing elit, sed do eiusmod tempor incid</p>
  <div class="hex" style="left:94px" role="img" aria-label="Government building with rooftop solar panels"><div style="position:absolute;inset:0;background:linear-gradient(180deg,#9fc4dc,#7b6a5e 60%,#3c4f63)"></div><div class="label">Government</div></div>
  <div class="hex" style="left:351px" role="img" aria-label="Solar farm with power pylons"><div style="position:absolute;inset:0;background:linear-gradient(180deg,#bcd6ea,#5f82a8 55%,#1e3f6e)"></div><div class="label">Infrastructure</div></div>
  <div class="hex" style="left:608px" role="img" aria-label="Solar carport over a commercial car park"><div style="position:absolute;inset:0;background:linear-gradient(180deg,#a8cbe6,#3f6e9e 50%,#263b55)"></div><div class="label">Commercial</div></div>
  <div class="hex" style="left:865px" role="img" aria-label="Residential house with solar panels on a brown roof"><div style="position:absolute;inset:0;background:linear-gradient(180deg,#cfe1ee,#6b4a3c 50%,#3e4c5c)"></div><div class="label">Residential</div></div>
  <svg class="abs" style="left:0;top:1880px" width="1200" height="130" viewBox="0 0 1200 130">
    <polygon points="0,128 600,8 1200,128 1200,130 0,130" fill="#eef1f4"/>
    <polyline points="0,128 600,8 1200,128" fill="none" stroke="#0b5fa8" stroke-width="8"/>
  </svg>
  <div class="abs" style="left:599px;top:1840px;width:1px;height:110px;background:rgba(255,255,255,.5)"></div>
</section>

<section class="gutter">
  <div class="abs gutter-bg"></div>
  <div class="photo gutter-photo" role="img" aria-label="Worker in a harness cleaning gutters on a terracotta tiled roof"></div>
  <h2 class="gutter-title">Gutter Cleaning</h2>
  <p class="gutter-text">Lorem ipsum dolor sit amet, consectetur adipiscing elit, sed do eiusmod</p>
  <div class="corner" style="left:506px;top:2063px;width:70px;height:60px;border-width:10px 0 0 10px"></div>
  <div class="corner" style="left:1080px;top:2370px;width:68px;height:86px;border-width:0 10px 10px 0"></div>
  <div class="tile" style="left:517px;top:2075px" role="img" aria-label="Modern government office building with glass facade"><div style="position:absolute;inset:0;background:linear-gradient(180deg,#6ea7dc,#9aa7b4 55%,#2c3440)"></div><div class="label">Government</div></div>
  <div class="tile" style="left:833px;top:2029px" role="img" aria-label="Layered sandstone rock face"><div style="position:absolute;inset:0;background:linear-gradient(180deg,#e2b3a3,#c98f80 50%,#b88375)"></div><div class="label">Strata</div></div>
  <div class="tile" style="left:517px;top:2291px" role="img" aria-label="Flat commercial roof with skylights"><div style="position:absolute;inset:0;background:linear-gradient(180deg,#c7d8e6,#4a5f78 50%,#2a3a4e)"></div><div class="label">Commercial</div></div>
  <div class="tile" style="left:833px;top:2245px" role="img" aria-label="Grey residential roof with dormer windows"><div style="position:absolute;inset:0;background:linear-gradient(180deg,#dbe6ef,#7c8790 50%,#4a535c)"></div><div class="label">Residential</div></div>
  <div class="abs" style="left:599px;top:2560px;width:1px;height:110px;background:#c9d3dd"></div>
</section>

<section class="testimonials">
  <h2 class="section-title testi-title">What People Says</h2>
  <div class="side-card">
    <p style="left:44px">“Lorem ipsum dolor sit amet consectetur adipiscing elit sed do eiusmod tempor incididunt ut labore enim ad minim veniam nisi ut aliquip ex ea reprehenderit in voluptate</p>
    <p style="right:44px;width:120px;text-align:left">adipiscing elit sed do eiusmod dolore magna aliqua ut enim ad exercitation ullamco laboris nisi duis aute irure dolor in reprehenderit dolore eu fugiat nulla</p>
    <span class="g"></span>
  </div>
  <div class="corner" style="left:306px;top:2773px;width:90px;height:70px;border-width:8px 0 0 8px"></div>
  <div class="corner" style="left:816px;top:3030px;width:90px;height:76px;border-width:0 8px 8px 0"></div>
  <div class="main-quote">
    <div class="qm">“</div>
    <p>“Lorem ipsum dolor sit amet, consectetur adipiscing elit, sed do eius-mod tempor incididunt ut labore et dolore magna aliqua. Ut enim ad minim veniam, quis nostrud exercitation ullamco laboris nisi ut aliquip ex ea commodo consequat. Duis aute irure dolor in reprehenderit in voluptate velit esse cillum dolore eu”</p>
    <div class="stars">★★★★★</div>
    <div class="name">Liam Carter</div>
    <span class="g"></span>
  </div>
  <div class="arrow" style="left:85px"><svg width="20" height="14" viewBox="0 0 20 14"><path d="M19 7H2M7 1L1 7l6 6" fill="none" stroke="#1d3557" stroke-width="1.8"/></svg></div>
  <div class="arrow" style="left:1081px"><svg width="20" height="14" viewBox="0 0 20 14"><path d="M1 7h17M13 1l6 6-6 6" fill="none" stroke="#1d3557" stroke-width="1.8"/></svg></div>
</section>

<section class="request">
  <div class="photo houses-photo" role="img" aria-label="Suburban houses with solar panels covering their roofs"></div>
  <div class="quote-box">
    <h2 class="quote-title">Request a Quote</h2>
  </div>
  <div class="field" style="left:267px;top:3447px;width:340px"><svg width="16" height="16" viewBox="0 0 16 16"><circle cx="8" cy="5" r="3.5" fill="none" stroke="#8a949e"/><path d="M1.5 15c0-3.5 3-5.5 6.5-5.5s6.5 2 6.5 5.5" fill="none" stroke="#8a949e"/></svg>First Name*</div>
  <div class="field" style="left:616px;top:3447px;width:340px"><svg width="16" height="16" viewBox="0 0 16 16"><circle cx="8" cy="5" r="3.5" fill="none" stroke="#8a949e"/><path d="M1.5 15c0-3.5 3-5.5 6.5-5.5s6.5 2 6.5 5.5" fill="none" stroke="#8a949e"/></svg>Last Name*</div>
  <div class="field" style="left:267px;top:3512px;width:340px"><svg width="18" height="14" viewBox="0 0 18 14"><rect x=".5" y=".5" width="17" height="13" fill="none" stroke="#8a949e"/><path d="M.5 .5l8.5 7 8.5-7" fill="none" stroke="#8a949e"/></svg>E-mail*</div>
  <div class="field" style="left:616px;top:3512px;width:340px"><svg width="16" height="16" viewBox="0 0 16 16"><path d="M3 1l3 3-2 2c1 2.5 3.5 5 6 6l2-2 3 3-2 2C7 14 2 9 1 3z" fill="none" stroke="#8a949e"/></svg>Phone number*</div>
  <div class="field msg" style="left:267px;top:3572px;width:689px;height:111px"><svg width="18" height="18" viewBox="0 0 18 18"><path d="M9 1.5a7.5 7 0 1 0 0 14c1.2 0 2.3-.2 3.3-.6L16 16l-1-3.3A7 7 0 0 0 16.5 8.5 7.5 7 0 0 0 9 1.5z" fill="none" stroke="#8a949e"/></svg>Leave Message</div>
  <div class="btn" style="left:517px;top:3709px;width:192px;background:var(--navy)"><i class="notch"></i><span>SEND MESSAGE ›</span></div>
</section>

<footer class="site-footer">
  <div class="abs footer-mark"></div>
  <div class="abs footer-brand">PanelBrite</div>
  <div class="socials"><span></span><span></span><span></span><span></span><span></span></div>

  <div class="fcol" style="left:385px">
    <h4>NAVIGATION</h4>
    <ul><li>Home</li><li>Solar Cleaning</li><li>Gutter Cleaning</li><li>Resellers Portal</li><li>Customer portal</li><li>Contact Us</li></ul>
  </div>
  <div class="fcol" style="left:585px">
    <h4>CONTACT US</h4>
    <ul style="margin-top:20px">
      <li><svg width="12" height="12" viewBox="0 0 16 16"><path d="M3 1l3 3-2 2c1 2.5 3.5 5 6 6l2-2 3 3-2 2C7 14 2 9 1 3z" fill="#1b8fd6"/></svg>Sydney – 02 7391 5084</li>
      <li><svg width="12" height="12" viewBox="0 0 16 16"><path d="M3 1l3 3-2 2c1 2.5 3.5 5 6 6l2-2 3 3-2 2C7 14 2 9 1 3z" fill="#1b8fd6"/></svg>Southern Highlands – 02 4863 1507</li>
      <li><svg width="12" height="12" viewBox="0 0 16 16"><path d="M3 1l3 3-2 2c1 2.5 3.5 5 6 6l2-2 3 3-2 2C7 14 2 9 1 3z" fill="#1b8fd6"/></svg>Goulburn – 02 4863 1507</li>
      <li><svg width="12" height="12" viewBox="0 0 16 16"><path d="M3 1l3 3-2 2c1 2.5 3.5 5 6 6l2-2 3 3-2 2C7 14 2 9 1 3z" fill="#1b8fd6"/></svg>Canberra – 02 6178 3045</li>
      <li><svg width="12" height="12" viewBox="0 0 16 16"><path d="M3 1l3 3-2 2c1 2.5 3.5 5 6 6l2-2 3 3-2 2C7 14 2 9 1 3z" fill="#1b8fd6"/></svg>Wollongong – 02 4239 7615</li>
    </ul>
  </div>
  <div class="fcol" style="left:881px">
    <h4>GET IN TOUCH</h4>
    <ul style="margin-top:20px">
      <li><svg width="16" height="12" viewBox="0 0 18 14"><rect width="18" height="14" fill="#1b8fd6"/><path d="M1 1l8 6.5L17 1" fill="none" stroke="#fff" stroke-width="1.5"/></svg>sales@panelbrite.com.au</li>
      <li style="margin-top:18px;align-items:flex-start"><svg width="14" height="18" viewBox="0 0 14 18" style="margin-top:3px"><path d="M7 0a7 7 0 0 1 7 7c0 5-7 11-7 11S0 12 0 7a7 7 0 0 1 7-7z" fill="#1b8fd6"/><circle cx="7" cy="7" r="2.5" fill="#fff"/></svg><span>Head Office -<br>Ferndell NSW 2583<br>ABN: 48762093115</span></li>
    </ul>
  </div>
  <div class="copyright">Copyright © 2025 PanelBrite. All Right Reserved</div>
</footer>

</body>
</html>
```